Education related business need name card design

We need name card design for long term study agent.
Company name is Harbor Lantern.
We support clients to connect to the world.
Clients are Japanese family who has primary and secondary school students.

Company Logo is reflection of the globe and HL (Harbor Lantern).
Since business is related to education, we would like to show reliability and love to see the world map (atlas) in the name card.

Target Market(s)

late 30's to 50's parents of primary and secondary students who are enthusiastic for education. Secondary school management

Industry/Entity Type

Education

Contact Information for Business Card

Company name, Address, Official position, Name, Phone number, Mobile number, email address,

Font styles to use
Serif
Other font styles liked:
• Century Gothic(logo)

Requirements
Must have
• Since businee is related to education, we would like to show reliability and love to see the world map (atlas) in the name card.

```html
<!DOCTYPE html>
<html lang="en">
<head>
<meta charset="utf-8">
<title>Harbor Lantern – Business Card</title>
<link href="https://fonts.googleapis.com/css2?family=Source+Serif+4:wght@400;600;700&display=swap" rel="stylesheet">
<style>
  :root{
    --stage:#2b2c2e;
    --navy:#0a3f93;
    --navy-deep:#063381;
    --navy-map:#1a56ad;
    --brand-blue:#1f7fd6;
    --brand-dark:#0c3f8c;
    --ink:#555555;
    --paper:#ffffff;
    --map-tint:#cfe2f4;
    --map-soft:#e6f0f9;
    --divider:#c9c9c9;
    --faint-blue:#3b78d8;
  }
  *{margin:0;padding:0;box-sizing:border-box}
  html,body{width:1200px;height:950px;overflow:hidden}
  body{background:var(--stage);font-family:"Source Serif 4",Georgia,serif;position:relative}

  .card{position:absolute;left:250px;width:700px;height:400px;overflow:hidden;box-shadow:0 10px 30px rgba(0,0,0,.45)}

  /* Front */
  .card--front{top:45px;background:linear-gradient(135deg,var(--navy) 0%,var(--navy-deep) 100%)}
  .card--front .atlas{position:absolute;inset:0;
    background:radial-gradient(ellipse 60% 55% at 55% 45%,rgba(26,86,173,.75) 0%,rgba(26,86,173,.3) 55%,rgba(26,86,173,0) 80%)}
  .front-mark{position:absolute;left:50%;top:146px;transform:translateX(-50%);display:flex;align-items:center;gap:16px;color:var(--faint-blue);font-size:36px;font-weight:400;white-space:nowrap}
  .front-mark .dot{width:26px;height:26px;border-radius:50%;background:var(--faint-blue)}
  .front-url{position:absolute;left:0;right:0;top:298px;text-align:center;color:#d5e2f5;font-size:15px;letter-spacing:3px}

  /* Back */
  .card--back{top:505px;background:var(--paper)}
  .card--back .atlas{position:absolute;inset:0;
    background:
      radial-gradient(ellipse 45% 40% at 68% 28%,var(--map-tint) 0%,rgba(207,226,244,0) 100%),
      radial-gradient(ellipse 40% 45% at 92% 75%,var(--map-soft) 0%,rgba(230,240,249,0) 100%),
      radial-gradient(ellipse 30% 30% at 40% 18%,var(--map-soft) 0%,rgba(230,240,249,0) 100%)}
  .brand{position:absolute;left:60px;top:60px;display:flex;align-items:center;gap:18px}
  .brand .dot{width:70px;height:70px;border-radius:50%;background:var(--brand-blue)}
  .brand-name{color:var(--brand-dark);font-size:34px;font-weight:400;line-height:1.08}
  .holder{position:absolute;left:30px;top:212px;width:280px;text-align:right}
  .holder-name{color:var(--brand-blue);font-size:22px;font-weight:700}
  .holder-role{color:var(--brand-blue);font-size:17px;margin-top:2px}
  .holder-address{color:var(--ink);font-size:16px;line-height:1.45;margin-top:8px}
  .divider{position:absolute;left:330px;top:230px;width:1px;height:120px;background:var(--divider)}
  .contacts{position:absolute;left:350px;top:232px;list-style:none}
  .contacts li{display:flex;align-items:center;gap:12px;color:var(--ink);font-size:17px;height:29px;white-space:nowrap}
  .contacts svg{width:18px;height:18px;fill:var(--brand-blue);flex:none}
</style>
</head>
<body>

<section class="card card--front" aria-label="Card front">
  <div class="atlas" role="img" aria-label="Faint world map in deep blue"></div>
  <div class="front-mark"><span class="dot"></span>Harbor Lantern</div>
  <p class="front-url">www.harborlantern.example</p>
</section>

<section class="card card--back" aria-label="Card back">
  <div class="atlas" role="img" aria-label="Soft world map in pale blue"></div>

  <div class="brand">
    <span class="dot"></span>
    <div class="brand-name">Harbor Lantern<br>Pte.Ltd.</div>
  </div>

  <div class="holder">
    <p class="holder-name">Mara Quill</p>
    <p class="holder-role">President</p>
    <p class="holder-address">2716 Alder Crest Lane<br>Brookvale, NY 10482</p>
  </div>

  <div class="divider"></div>

  <ul class="contacts">
    <li><svg viewBox="0 0 24 24"><path d="M6.6 10.8a15.1 15.1 0 0 0 6.6 6.6l2.2-2.2c.3-.3.7-.4 1-.2 1.1.4 2.3.6 3.6.6.6 0 1 .4 1 1V20c0 .6-.4 1-1 1A17 17 0 0 1 3 4c0-.6.4-1 1-1h3.5c.6 0 1 .4 1 1 0 1.3.2 2.5.6 3.6.1.3 0 .7-.2 1z"/></svg>555 0142 7781</li>
    <li><svg viewBox="0 0 24 24"><path d="M7 1h10a2 2 0 0 1 2 2v18a2 2 0 0 1-2 2H7a2 2 0 0 1-2-2V3a2 2 0 0 1 2-2zm0 3v14h10V4zm5 15.5a1.2 1.2 0 1 0 0 2.4 1.2 1.2 0 0 0 0-2.4z"/></svg>555 0193 4406</li>
    <li><svg viewBox="0 0 24 24"><path d="M2 5h20v14H2zm2 2v.5l8 5 8-5V7zm0 2.9V17h16V9.9l-8 5z"/></svg>mara@harborlantern.example</li>
    <li><svg viewBox="0 0 24 24"><path d="M12 2a10 10 0 1 0 0 20 10 10 0 0 0 0-20zm0 4a3 3 0 1 1 0 6 3 3 0 0 1 0-6zm0 14a8 8 0 0 1-6-2.7c.6-1.9 3-3.3 6-3.3s5.4 1.4 6 3.3A8 8 0 0 1 12 20z"/></svg>www.harborlantern.example</li>
  </ul>
</section>

</body>
</html>
```